Business Cards Needed

Hi designers, I have a new logo that was created by one of the ArtMingle designers. I'd now like to use that logo to make business cards. The company is called VitaLumen Advisors and is a business consulting firm. I'd like the business cards to be horizontal, modern, and professional.
I'd like the following information to be on the business card:
1) Logo
2) my name - Marisa Kolvane
3) my title - Principal
4) name of business - VitaLumen Advisors
5) mobile - 508.372.9146
6) e-mail - marisa@vitalumenadvisors.example
I'm uploading a JPG file of the logo. I'm hoping this is the correct file format. Please let me know if you need another type of file. Thank you.
Look and feel
Each slider illustrates characteristics of the customer's brand and the style your logo design should communicate.

```html
<!DOCTYPE html>
<html lang="en">
<head>
<meta charset="utf-8">
<title>VitaLumen Advisors – Business Card</title>
<link rel="stylesheet" href="https://fonts.googleapis.com/css2?family=Open+Sans:wght@400;700&display=swap">
<style>
  :root {
    --backdrop: #4a4a4a;
    --card: #151515;
    --edge: #1f78d1;
    --brand-blue: #2a86d8;
    --accent-green: #8cc63f;
    --text-light: #f2f2f2;
    --emboss: #2c2c2c;
  }
  * { margin: 0; padding: 0; box-sizing: border-box; }
  html, body {
    width: 1200px; height: 800px; overflow: hidden;
    background: var(--backdrop);
    font-family: "Open Sans", Arial, sans-serif;
  }
  .canvas {
    width: 1200px; height: 800px;
    display: flex; flex-direction: column;
    align-items: center; justify-content: center; gap: 44px;
  }
  .card {
    width: 616px; height: 352px;
    background: var(--card);
    border-radius: 22px;
    border: 2px solid var(--edge);
    position: relative; overflow: hidden;
  }
  /* Front */
  .card-front { display: flex; align-items: center; }
  .front-brand {
    width: 300px; display: flex; align-items: center; justify-content: center; gap: 10px;
  }
  .brand-dot {
    width: 14px; height: 14px; border-radius: 50%; background: var(--accent-green);
  }
  .brand-name {
    color: var(--brand-blue); font-weight: 400; font-size: 25px; letter-spacing: 0.5px;
  }
  .front-divider {
    width: 1.5px; height: 190px; background: var(--edge);
  }
  .front-details { padding-left: 28px; }
  .person-name {
    color: var(--brand-blue); font-weight: 700; font-size: 24px; letter-spacing: 1.5px;
    text-transform: uppercase; line-height: 1.1;
  }
  .person-title {
    color: var(--text-light); font-size: 15px; margin: 4px 0 16px;
  }
  .contact-list { list-style: none; }
  .contact-item {
    display: flex; align-items: center; gap: 9px;
    color: var(--text-light); font-size: 13px; line-height: 1.9;
  }
  .contact-icon { width: 13px; height: 13px; flex: none; }
  /* Back */
  .card-back { display: flex; align-items: center; justify-content: center; }
  .back-brand {
    color: var(--emboss); font-weight: 700; font-size: 50px; letter-spacing: 1px;
  }
</style>
</head>
<body>
<main class="canvas">
  <section class="card card-front" aria-label="Card front">
    <div class="front-brand">
      <span class="brand-dot"></span>
      <span class="brand-name">VitaLumen Advisors</span>
    </div>
    <div class="front-divider"></div>
    <div class="front-details">
      <h1 class="person-name">Marisa Kolvane</h1>
      <p class="person-title">Principal</p>
      <ul class="contact-list">
        <li class="contact-item">
          <svg class="contact-icon" viewBox="0 0 16 16" aria-hidden="true"><path fill="var(--accent-green)" d="M3.5 1l3 3-2 2c1 2 3 4 5 5l2-2 3 3-2 3C7 15 1 9 1 3.5z"/></svg>
          508.372.9146
        </li>
        <li class="contact-item">
          <svg class="contact-icon" viewBox="0 0 16 16" aria-hidden="true"><rect x="1" y="3" width="14" height="10" fill="var(--accent-green)"/><path d="M1 3l7 6 7-6" fill="none" stroke="var(--card)" stroke-width="1.4"/></svg>
          marisa@vitalumenadvisors.example
        </li>
        <li class="contact-item">
          <svg class="contact-icon" viewBox="0 0 16 16" aria-hidden="true"><circle cx="8" cy="8" r="7" fill="var(--accent-green)"/><path d="M1 8h14M8 1c-3 4-3 10 0 14M8 1c3 4 3 10 0 14" fill="none" stroke="var(--card)" stroke-width="1.1"/></svg>
          www.vitalumenadvisors.example
        </li>
      </ul>
    </div>
  </section>

  <section class="card card-back" aria-label="Card back">
    <span class="back-brand">VitaLumen Advisors</span>
  </section>
</main>
</body>
</html>
```